Business Card for By Karel Voss

Looking to have a business card designed for my lifestyle and fitness company. My company offers personal training, online programming and nutrition advice based out of London, United Kingdom.

I'd like to see modern, sleek designs, focusing on black, matte black or matte grey. Design doesn't need to be overly descriptive as this will also be used as a personal business card. I've included my logo.

Please note that my company is no longer called "Fitness by Karel Voss" but instead "By Karel Voss", this is because of my other ventures. Therefore please don't use the "fitness by karel voss" text.

information about my company can be found at www.bykarelvoss.com

Company is also based out of London (United Kingdom) & Sydney (Australia) this could be reflected on the card.

Industry/Entity Type

Business

Contact Information for Business Card

Karel Voss
+44 7382 615027
karel@bykarelvoss.com
www.bykarelvoss.com

Font styles to use
Sans Serif

Requirements
Must have
• All contact details and inclusion of my logo.

```html
<!DOCTYPE html>
<html lang="en">
<head>
<meta charset="utf-8">
<title>By Karel Voss — Business Card</title>
<link rel="stylesheet" href="https://fonts.googleapis.com/css2?family=Oswald:wght@500&family=Jost:wght@400;500&display=swap">
<style>
  :root {
    --backdrop: #2b2b2c;
    --card: #161616;
    --card-edge: #222;
    --ink: #f2f2f2;
    --ink-soft: #c9c9c9;
    --silver: #8e8e90;
    --rule: #d8d8d8;
  }
  * { margin: 0; padding: 0; box-sizing: border-box; }
  html, body {
    width: 1200px; height: 900px; overflow: hidden;
    background: var(--backdrop);
    font-family: "Jost", sans-serif;
  }
  .sheet {
    width: 1200px; height: 900px;
    display: flex; flex-direction: column; align-items: center; justify-content: center;
    gap: 36px;
  }
  .card {
    position: relative;
    width: 700px; height: 400px;
    background: var(--card);
    border: 1px solid var(--card-edge);
    box-shadow: 0 14px 30px rgba(0,0,0,.45);
  }
  /* front */
  .card-front { display: flex; flex-direction: column; align-items: center; }
  .brand {
    margin-top: 120px;
    display: flex; align-items: center; gap: 14px;
  }
  .brand-mark {
    width: 34px; height: 34px;
    background: var(--silver);
  }
  .brand-name {
    font-family: "Jost", sans-serif;
    font-weight: 500;
    font-size: 32px;
    letter-spacing: 2px;
    text-transform: uppercase;
    color: var(--silver);
  }
  .front-web {
    position: absolute; bottom: 62px; left: 0; right: 0;
    text-align: center;
    font-size: 15px;
    letter-spacing: 7px;
    color: var(--ink-soft);
  }
  /* back */
  .identity {
    position: absolute; right: 390px; top: 138px;
    text-align: right;
  }
  .person-name {
    font-family: "Oswald", sans-serif;
    font-weight: 500;
    font-size: 44px;
    line-height: 1;
    color: var(--ink);
    letter-spacing: 1px;
  }
  .person-role {
    margin-top: 8px;
    font-size: 21px;
    color: var(--ink);
    letter-spacing: 1px;
  }
  .divider {
    position: absolute; left: 330px; top: 140px;
    width: 2px; height: 80px;
    background: var(--rule);
  }
  .contacts {
    position: absolute; left: 350px; top: 142px;
    list-style: none;
  }
  .contacts li {
    display: flex; align-items: center; gap: 12px;
    font-size: 20px;
    line-height: 26px;
    color: var(--ink);
  }
  .contacts svg { width: 18px; height: 18px; flex: none; }
  .location {
    position: absolute; left: 44px; bottom: 52px;
    font-size: 19px;
    color: var(--ink);
    letter-spacing: .5px;
  }
</style>
</head>
<body>
<main class="sheet">
  <section class="card card-front">
    <div class="brand">
      <span class="brand-mark" aria-hidden="true"></span>
      <span class="brand-name">By Karel Voss</span>
    </div>
    <p class="front-web">www.bykarelvoss.com</p>
  </section>

  <section class="card card-back">
    <div class="identity">
      <h1 class="person-name">KAREL VOSS</h1>
      <p class="person-role">CEO &amp; FOUNDER</p>
    </div>
    <span class="divider" aria-hidden="true"></span>
    <ul class="contacts">
      <li>
        <svg viewBox="0 0 24 24" aria-hidden="true"><path d="M6.6 2.5l3 3.2-1.8 2.4c1.3 2.8 3.4 4.9 6.1 6.2l2.4-1.8 3.2 3-1.8 3.4C10.5 18.7 5.2 13.4 3.4 4.3z" fill="none" stroke="#d0d0d0" stroke-width="2" stroke-linejoin="round"/></svg>
        <span>44 7382 615027</span>
      </li>
      <li>
        <svg viewBox="0 0 24 24" aria-hidden="true"><rect x="2" y="5" width="20" height="14" fill="#d0d0d0"/><path d="M2 5l10 8 10-8" fill="none" stroke="#161616" stroke-width="2"/></svg>
        <span>karel@bykarelvoss.com</span>
      </li>
      <li>
        <svg viewBox="0 0 24 24" aria-hidden="true"><circle cx="13" cy="10" r="7" fill="none" stroke="#d0d0d0" stroke-width="2"/><path d="M8 15l-5 5" stroke="#d0d0d0" stroke-width="2.5" stroke-linecap="round"/></svg>
        <span>www.bykarelvoss.com</span>
      </li>
    </ul>
    <p class="location">Location : London, United Kingdom &amp; Sydney, Australia</p>
  </section>
</main>
</body>
</html>
```